Business Card design for a skin clinic

i would like a business card design for our skin clinic.
our logo colors are Blue and Grey and Bule /white.
we are searching for a minimalistic design yet very elegant,dynamic and professional which can reflect a professional medical skin care clinic( not a beauty salon).
THE DESGIN IS NOT FOR A PERSON IT WILL BE USED IN THE CLINIC FOR CLIENTS SO THERE SHOULD BE NO NAME OF A PERSON ONLY THE CLINIC NAME AND THE CONTACT INFO

Target Market(s)
young and old womens
Industry/Entity Type
Business
Contact Information for Business Card
we have 2 address and both should be on the card.
address A: Lindenhoflaan 214B, 3041KP Rotterdam, Tel 010 483 21 95
address B: Zonnewijzerstraat 238, 1062RT Amsterdam Tel 020 571 3829
website www.huidpuntzorg.nu, email info@huidpuntzorg.nu
Look and feel
Each slider illustrates characteristics of the customer's brand and the style your logo design should communicate.

```html
<!DOCTYPE html>
<html lang="nl">
<head>
<meta charset="utf-8">
<title>Huidpuntzorg – Business Card</title>
<link rel="stylesheet" href="https://fonts.googleapis.com/css2?family=Montserrat:wght@400;500&family=Open+Sans:wght@300;400&display=swap">
<style>
  :root {
    --backdrop: #c6c5c6;
    --card-dark: #141a22;
    --card-mid: #222933;
    --card-light: #2e3540;
    --brand-blue: #3a8fd6;
    --text-white: #f2f4f6;
    --text-grey: #aab1ba;
    --shadow: rgba(20, 24, 30, 0.35);
  }
  * { margin: 0; padding: 0; box-sizing: border-box; }
  html, body {
    width: 1200px; height: 1000px; overflow: hidden;
    background: var(--backdrop);
  }
  .canvas { position: relative; width: 1200px; height: 1000px; }
  .card {
    position: absolute; left: 270px; width: 660px; height: 378px;
    border-radius: 34px; overflow: hidden;
    box-shadow: 0 14px 30px var(--shadow);
  }
  .card--front {
    top: 92px;
    background: radial-gradient(ellipse at 55% 30%, var(--card-light) 0%, var(--card-mid) 45%, var(--card-dark) 100%);
  }
  .card--back {
    top: 530px;
    background: linear-gradient(160deg, var(--card-mid) 0%, var(--card-dark) 100%);
  }
  .world-map {
    position: absolute; left: 40px; top: 20px; width: 580px; height: 330px;
    border-radius: 50%;
    background: radial-gradient(ellipse at center, rgba(70,80,94,0.45) 0%, rgba(50,58,70,0.2) 55%, transparent 75%);
  }
  .brand { display: flex; align-items: center; gap: 10px; }
  .brand__dot {
    width: 14px; height: 14px; border-radius: 50%; background: var(--brand-blue); flex: none;
  }
  .brand__name {
    font-family: "Montserrat", sans-serif; font-weight: 500;
    color: var(--brand-blue); letter-spacing: 3px; text-transform: uppercase;
    white-space: nowrap;
  }
  .tagline {
    font-family: "Montserrat", sans-serif; font-weight: 400;
    color: var(--text-grey); letter-spacing: 2.5px; text-transform: lowercase;
    white-space: nowrap;
  }
  .front-content {
    position: absolute; inset: 0;
    display: flex; flex-direction: column; align-items: center; justify-content: center;
    padding-top: 10px;
  }
  .front-content .brand__name { font-size: 40px; }
  .front-content .tagline { font-size: 15px; margin-top: 12px; }
  .front-content .web {
    margin-top: 58px; font-family: "Open Sans", sans-serif; font-size: 16px;
    letter-spacing: 4px; color: var(--text-white);
  }
  .accent { color: var(--brand-blue); }

  .contact {
    position: absolute; left: 48px; top: 52px;
    font-family: "Open Sans", sans-serif; font-weight: 300; font-size: 16px;
    color: var(--text-grey); line-height: 1.45;
  }
  .contact__rule {
    width: 96px; height: 3px; background: var(--brand-blue); margin-bottom: 16px;
  }
  .contact__row { display: flex; align-items: flex-start; gap: 12px; }
  .contact__row + .contact__row { margin-top: 3px; }
  .contact__row--gap { margin-top: 12px !important; }
  .contact__row svg {
    width: 14px; height: 14px; fill: var(--brand-blue); flex: none; margin-top: 5px;
  }
  .contact__text { white-space: nowrap; }

  .back-brand {
    position: absolute; right: 44px; top: 140px;
    display: flex; flex-direction: column; align-items: flex-start;
  }
  .back-brand .brand__name { font-size: 26px; }
  .back-brand .tagline { font-size: 11px; margin-top: 8px; margin-left: 24px; }
</style>
</head>
<body>
<main class="canvas">

  <section class="card card--front" aria-label="Card front">
    <div class="world-map" role="img" aria-label="Faint world map background"></div>
    <div class="front-content">
      <div class="brand">
        <span class="brand__dot"></span>
        <span class="brand__name">Huidpuntzorg</span>
      </div>
      <p class="tagline">next generation skin care</p>
      <p class="web">www.<span class="accent">huidpuntzorg</span>.nu</p>
    </div>
  </section>

  <section class="card card--back" aria-label="Card back">
    <div class="contact">
      <div class="contact__rule"></div>

      <p class="contact__row">
        <svg viewBox="0 0 24 24" aria-hidden="true"><path d="M12 2a7 7 0 0 0-7 7c0 5.2 7 13 7 13s7-7.8 7-13a7 7 0 0 0-7-7zm0 9.5A2.5 2.5 0 1 1 12 6.5a2.5 2.5 0 0 1 0 5z"/></svg>
        <span class="contact__text">Lindenhoflaan 214B,<br>3041KP Rotterdam</span>
      </p>
      <p class="contact__row">
        <svg viewBox="0 0 24 24" aria-hidden="true"><path d="M6.6 10.8a15.1 15.1 0 0 0 6.6 6.6l2.2-2.2a1 1 0 0 1 1-.25 11.4 11.4 0 0 0 3.6.57 1 1 0 0 1 1 1V20a1 1 0 0 1-1 1A17 17 0 0 1 3 4a1 1 0 0 1 1-1h3.5a1 1 0 0 1 1 1c0 1.25.2 2.45.57 3.57a1 1 0 0 1-.25 1z"/></svg>
        <span class="contact__text">010 483 21 95</span>
      </p>

      <p class="contact__row contact__row--gap">
        <svg viewBox="0 0 24 24" aria-hidden="true"><path d="M12 2a7 7 0 0 0-7 7c0 5.2 7 13 7 13s7-7.8 7-13a7 7 0 0 0-7-7zm0 9.5A2.5 2.5 0 1 1 12 6.5a2.5 2.5 0 0 1 0 5z"/></svg>
        <span class="contact__text">Zonnewijzerstraat 238,<br>1062RT Amsterdam</span>
      </p>
      <p class="contact__row">
        <svg viewBox="0 0 24 24" aria-hidden="true"><path d="M6.6 10.8a15.1 15.1 0 0 0 6.6 6.6l2.2-2.2a1 1 0 0 1 1-.25 11.4 11.4 0 0 0 3.6.57 1 1 0 0 1 1 1V20a1 1 0 0 1-1 1A17 17 0 0 1 3 4a1 1 0 0 1 1-1h3.5a1 1 0 0 1 1 1c0 1.25.2 2.45.57 3.57a1 1 0 0 1-.25 1z"/></svg>
        <span class="contact__text">020 571 3829</span>
      </p>

      <p class="contact__row contact__row--gap">
        <svg viewBox="0 0 24 24" aria-hidden="true"><path d="M2 5h20v14H2zm2 2v.5l8 5 8-5V7l-8 5z"/></svg>
        <span class="contact__text">info@huidpuntzorg.nu</span>
      </p>
      <p class="contact__row">
        <svg viewBox="0 0 24 24" aria-hidden="true"><path d="M12 2a10 10 0 1 0 0 20 10 10 0 0 0 0-20zm6.9 6h-3a15.6 15.6 0 0 0-1.4-3.6A8 8 0 0 1 18.9 8zM12 4c.8 1.2 1.5 2.5 1.9 4h-3.8c.4-1.5 1.1-2.8 1.9-4zM4.3 14a8 8 0 0 1 0-4h3.4a16 16 0 0 0 0 4zm.8 2h3a15.6 15.6 0 0 0 1.4 3.6A8 8 0 0 1 5.1 16zm3-8h-3a8 8 0 0 1 4.4-3.6C8.9 5.5 8.4 6.7 8.1 8zM12 20c-.8-1.2-1.5-2.5-1.9-4h3.8c-.4 1.5-1.1 2.8-1.9 4zm2.3-6H9.7a14.7 14.7 0 0 1 0-4h4.6a14.7 14.7 0 0 1 0 4zm.2 5.6c.6-1.1 1.1-2.3 1.4-3.6h3a8 8 0 0 1-4.4 3.6zM16.3 14a16 16 0 0 0 0-4h3.4a8 8 0 0 1 0 4z"/></svg>
        <span class="contact__text">www.<span class="accent">huidpuntzorg</span>.nu</span>
      </p>
    </div>

    <div class="back-brand">
      <div class="brand">
        <span class="brand__dot"></span>
        <span class="brand__name">Huidpuntzorg</span>
      </div>
      <p class="tagline">next generation skin care</p>
    </div>
  </section>

</main>
</body>
</html>
```